LumaForm Informational Flyer Design

Hello, we are a team of two who opened an all women's gym located in Seattle, WA. We've been in business for four and a half years renting from various other facilities such as crossfit, a banquet hall, and outside at local parks, and opened our own facility in January 2016.
Check www.lumaformstudio.example for more info about our gym, our team, and what we offer to our clients.
We are looking for a strong, clean, but feminine double-sided leaflet or something a little larger than the average postcard to pass out to local businesses, schools and other charitable auctions, and neighboring apartment buildings that are currently under construction. DL size
We have more images should you need them for the design, some more abstract of just equipment; included a few here along with our logo.
Please let me know if you need more info or more pics.
Thanks in advance!

Hello, I have updated the brief with more specifics. Please take a look and resubmit with thanks. Added Thursday, February 16, 2017

Target Market(s)

Women ages 18-70

Industry/Entity Type

Fitness

Font styles to use
Other font styles liked:
• Futura (SEE NOTES)

Colors
e34197
000000

Requirements
Must have
• DL Size
• Front should be clean and simple and include:
• • LOGO
• • RESULTS-DRIVEN WOMEN’S FITNESS
• • FREE INTRODUCTORY WEEK
• • pictures of LUMASPRINT, LUMAPOISE, & LUMASTILL with names overlaid on pictures (see home page of website)
• ◦ *CHILDCARE INCLUDED (underneath program pictures, but not too big)
• BACK side:
• • LumaForm is not just a women's gym. We are a community of women grinding and growing into the very best versions of ourselves.  LumaForm’s mission is simple -- to get you strong, balanced, and flexible for life both in and out of the gym.
• • PROGRAMS:   (Optional to include pictures of each program)
• LUMASPRINT underneath should list ASCEND & LUMABEGIN
• LUMAPOISE
• LUMASTILL underneath should list LUMA TIDE MOTION & RESTORATIVE YOGA
• • PRICING (includes childcare)
• ANNUAL $1675
• MONTHLY $159
• 10 CLASS PASS $199
• DROP-IN $25
• *See website for special discounts*
• • Phone
• • Email
• • Address
• • Website
• • COUPON CODE section with some space underneath to handwrite in a coupon code. 
Nice to have
• If it works with the design and doesn't make it too cluttered, instead of FREE INTRODUCTORY WEEK on front side, can say CLAIM YOUR FREE INTRO WEEK HERE (or some other wording) and include a QR code that goes directly to our scheduling site: https://lumaform.bookingdesk.example/hello
• Can use the fonts in the logo or designer preference on what will work best with design.

```html
<!DOCTYPE html>
<html lang="en">
<head>
<meta charset="utf-8">
<title>LumaForm DL Flyer</title>
<link href="https://fonts.googleapis.com/css2?family=Jost:ital,wght@0,400;0,500;0,600;0,700;1,700&display=swap" rel="stylesheet">
<style>
  :root{
    --stage:#0c80bf;
    --pink:#e0157f;
    --ink:#231f20;
    --black:#000;
    --white:#fff;
    --star:#f7941d;
    --grey-top:#ffffff;
    --grey-bottom:#dcdde1;
    --frame:#9a9a9a;
  }
  *{box-sizing:border-box;margin:0;padding:0}
  html,body{width:1200px;height:1000px;overflow:hidden}
  body{background:var(--stage);font-family:"Jost",sans-serif;position:relative}
  .card{position:absolute;top:148px;width:342px;height:704px;overflow:hidden}
  .front{left:199px;background:linear-gradient(#ececee,#d9dadd)}
  .back{left:658px;background:linear-gradient(var(--grey-top),var(--grey-bottom))}

  .photo{position:absolute;left:0;top:0;width:342px;height:470px;
    background:linear-gradient(180deg,#6b6a6a 0%,#8a7d76 35%,#5a4a4e 60%,#c86a98 85%,#b07a5c 100%)}
  .logo-band{position:absolute;left:-30px;top:432px;width:402px;height:112px}
  .brand{position:absolute;left:0;width:342px;text-align:center;color:var(--white)}
  .brand-name{top:458px;font-size:40px;font-weight:600;letter-spacing:1px;line-height:1}
  .brand-tag{top:498px;font-size:19px;font-weight:500;letter-spacing:1.5px;line-height:1}

  .headline{position:absolute;top:567px;left:0;width:342px;text-align:center;
    color:var(--pink);font-weight:700;font-size:20px;line-height:24px;letter-spacing:.3px}
  .star{position:absolute;width:20px;height:20px}
  .footer{position:absolute;left:0;top:637px;width:342px;height:67px;background:var(--black);
    color:var(--white);text-align:center;font-size:14.5px;line-height:25px;padding-top:6px}
  .footer sup{font-size:9px}

  .offer{position:absolute;top:33px;left:0;width:342px;text-align:center;color:var(--pink);
    font-size:15px;line-height:18px;text-transform:uppercase}
  .offer em{font-weight:700}
  .programs-title{position:absolute;top:142px;left:0;width:342px;text-align:center;color:var(--pink);
    font-weight:700;font-size:15px;line-height:18px}
  .program-list{position:absolute;top:193px;left:0;width:342px;list-style:none;text-align:center;
    font-size:14.5px;color:var(--ink)}
  .program-list li{height:32.2px;line-height:18px}
  .program-list .prefix{color:var(--pink)}
  .childcare{position:absolute;top:437px;left:0;width:342px;text-align:center;color:var(--pink);
    font-size:15px;line-height:18px}
  .childcare em{font-weight:700}
  .coupon-box{position:absolute;left:32px;top:503px;width:280px;height:171px;background:var(--white);
    border:1.5px solid var(--frame)}
  .coupon-brand{position:absolute;top:7px;left:0;width:100%;text-align:center;color:var(--ink)}
  .coupon-brand .name{display:block;font-size:17px;font-weight:700;line-height:17px}
  .coupon-brand .tag{display:block;font-size:7px;font-weight:600;letter-spacing:.6px;line-height:9px}
</style>
</head>
<body>

<section class="card front">
  <div class="photo" role="img" aria-label="Photo of women in black workout wear kneeling in a low lunge on pink yoga mats in a mirrored studio"></div>
  <svg class="logo-band" viewBox="0 0 402 112" aria-hidden="true"><ellipse cx="201" cy="56" rx="201" ry="56" fill="#000"/></svg>
  <div class="brand brand-name">LUMAFORM</div>
  <div class="brand brand-tag">YOU WILL ASCEND</div>

  <h1 class="headline">RESULTS-DRIVEN<br>WOMEN'S FITNESS</h1>
  <svg class="star" style="left:43px;top:582px" viewBox="0 0 20 20" aria-hidden="true"><polygon points="10,1 12.6,7.4 19.5,7.6 14.1,11.9 16,18.6 10,14.8 4,18.6 5.9,11.9 0.5,7.6 7.4,7.4" fill="var(--star)"/></svg>
  <svg class="star" style="left:279px;top:582px" viewBox="0 0 20 20" aria-hidden="true"><polygon points="10,1 12.6,7.4 19.5,7.6 14.1,11.9 16,18.6 10,14.8 4,18.6 5.9,11.9 0.5,7.6 7.4,7.4" fill="var(--star)"/></svg>

  <footer class="footer">
    <div>Info: 206.555.0147</div>
    <div>2750 36<sup>th</sup> Ave SW, Seattle, WA 98199</div>
  </footer>
</section>

<section class="card back">
  <p class="offer">Free <em>Intro Week</em> for all you<br>ladies<br>come and join our<br><em>Community</em></p>
  <svg class="star" style="left:59px;top:58px" viewBox="0 0 20 20" aria-hidden="true"><polygon points="10,1 12.6,7.4 19.5,7.6 14.1,11.9 16,18.6 10,14.8 4,18.6 5.9,11.9 0.5,7.6 7.4,7.4" fill="var(--star)"/></svg>
  <svg class="star" style="left:263px;top:58px" viewBox="0 0 20 20" aria-hidden="true"><polygon points="10,1 12.6,7.4 19.5,7.6 14.1,11.9 16,18.6 10,14.8 4,18.6 5.9,11.9 0.5,7.6 7.4,7.4" fill="var(--star)"/></svg>

  <h2 class="programs-title">EXPERIENCE<br>OUR OFFERED PROGRAMS:</h2>
  <ul class="program-list">
    <li><span class="prefix">LUMA</span>SPRINT</li>
    <li><span class="prefix">AS</span>CEND</li>
    <li><span class="prefix">LUMA</span>BEGIN</li>
    <li><span class="prefix">LUMA</span>POISE</li>
    <li><span class="prefix">LUMA</span>STILL</li>
    <li><span class="prefix">LUMA</span> ROW MOTION</li>
    <li><span class="prefix">RESTORATIVE</span> YOGA</li>
  </ul>

  <p class="childcare"><em>CHILD CARE</em> INCLUDED<br>IN OUR PROGRAMS</p>
  <svg class="star" style="left:64px;top:445px" viewBox="0 0 20 20" aria-hidden="true"><polygon points="10,1 12.6,7.4 19.5,7.6 14.1,11.9 16,18.6 10,14.8 4,18.6 5.9,11.9 0.5,7.6 7.4,7.4" fill="var(--star)"/></svg>
  <svg class="star" style="left:259px;top:445px" viewBox="0 0 20 20" aria-hidden="true"><polygon points="10,1 12.6,7.4 19.5,7.6 14.1,11.9 16,18.6 10,14.8 4,18.6 5.9,11.9 0.5,7.6 7.4,7.4" fill="var(--star)"/></svg>

  <div class="coupon-box">
    <div class="coupon-brand"><span class="name">LUMAFORM</span><span class="tag">YOU WILL ASCEND</span></div>
  </div>
</section>

</body>
</html>
```